ORVET - Helping People with Disabilities

ORVET is a nonprofit that strives to enable people with physical disabilities to live meaningful, quality lives. ORVET needs a professional attractive website that:
• establishes a strong brand image
• presents Orvet's services to those who need it
• raises funds from potential donors
Please see WORD DOC attached for more information about design vision.

Target Market(s)

people with disabilities

Industry/Entity Type

charity website

Number of Pages Required

2 page

Font styles to use
Sans Serif

Requirements
Must have
• 1. 2 pages means 1 design for homepage and 1 design for top of inner pages (banner ideas)
Nice to have
• please see attached design brief (WORD DOC)

```html
<!DOCTYPE html>
<html lang="en">
<head>
<meta charset="utf-8">
<title>ORVET – A good life for everyone</title>
<link href="https://fonts.googleapis.com/css2?family=Lora:wght@500;600;700&family=Poppins:ital,wght@0,400;0,500;0,600;1,500&display=swap" rel="stylesheet">
<style>
:root{
  --teal:#0b6b5f;
  --teal-dark:#075a50;
  --yellow:#e8b20e;
  --green:#3aaa47;
  --soft:#f3f5f4;
  --ink:#222;
  --muted:#555;
  --white:#fff;
  --line:#d8dcda;
}
*{box-sizing:border-box;margin:0;padding:0}
html,body{width:1200px;height:4850px;overflow:hidden}
body{position:relative;font-family:'Poppins',sans-serif;color:var(--ink);background:var(--white)}
.abs{position:absolute}
.serif{font-family:'Lora',serif}
.pill{position:absolute;display:flex;align-items:center;justify-content:center;border-radius:40px;font-weight:600;color:var(--white);text-transform:uppercase;font-size:16px}
.pill.yellow{background:var(--yellow)}
.pill.teal{background:var(--teal)}
.photo{position:absolute}

/* header */
.brand{position:absolute;left:110px;top:30px;display:flex;align-items:center;gap:10px;font-family:'Lora',serif;font-weight:700;font-size:30px;color:var(--teal)}
.brand .mark{width:22px;height:22px;background:var(--teal);border-radius:50%}
.social-top{position:absolute;top:15px;display:flex;gap:8px;left:946px}
.social-top span{width:40px;height:40px;border:1.5px solid #bbb;border-radius:50%;display:block;position:relative}
.social-top span::after{content:"";position:absolute;left:14px;top:14px;width:10px;height:10px;border-radius:50%;background:var(--green)}
.nav{position:absolute;top:78px;left:328px;display:flex;gap:23px;font-size:16px;color:#333}

/* hero */
.hero-panel{position:absolute;left:0;top:118px;width:482px;height:602px;background:var(--teal)}
.hero-rule{position:absolute;left:190px;top:233px;width:322px;height:6px;background:var(--green)}
.hero-title{position:absolute;left:110px;top:280px;font-size:54px;line-height:67px;color:var(--white);font-weight:600}

/* want to know */
.want{position:absolute;left:0;top:720px;width:1200px;height:530px;background:var(--soft)}
.section-title{position:absolute;width:100%;text-align:center;font-family:'Lora',serif;font-weight:600;font-size:40px}
.tri-text{position:absolute;width:170px;text-align:center;font-size:15px;line-height:22px;color:#333}

/* about */
.about-card{position:absolute;left:634px;top:1250px;width:454px;height:528px;background:var(--white)}
.eyebrow{font-size:19px;font-weight:600;color:var(--teal)}
.h2{font-family:'Lora',serif;font-weight:600;font-size:38px}
.body-text{font-size:15.5px;line-height:27px;color:var(--muted)}

/* services */
.services{position:absolute;left:0;top:1734px;width:1200px;height:718px;background:var(--green)}
.card{position:absolute;top:1978px;width:278px;height:387px;background:var(--white)}
.card .img{height:190px}
.card h3{margin:30px 20px 0;font-size:22px;font-weight:600;line-height:26px;color:#222}
.card p{margin:14px 20px 0;font-size:15px;line-height:24px;color:var(--muted)}

/* banner */
.banner-title{position:absolute;left:107px;top:2545px;font-family:'Lora',serif;font-weight:600;font-size:44px;line-height:54px;color:var(--white)}

/* news */
.news-item{position:absolute;left:110px;width:440px;height:140px}
.news-item .thumb{position:absolute;left:0;top:0;width:190px;height:140px}
.news-item h4{position:absolute;left:210px;top:0;font-size:19px;font-weight:500;line-height:28px;width:230px}
.news-item .date{position:absolute;left:210px;top:72px;font-size:15px;color:var(--muted);display:flex;gap:6px;align-items:center}
.news-item .date i{width:13px;height:13px;background:var(--green);border-radius:2px;display:block}

/* contact */
.contact{position:absolute;left:0;top:3730px;width:1200px;height:640px;background:var(--soft)}
.field{position:absolute;background:var(--white);border:1px solid var(--line);font-size:15px;color:#555;padding:13px 16px}

/* footer */
.foot-head{position:absolute;font-size:20px;font-weight:500;color:#222}
.foot-row{position:absolute;display:flex;align-items:center;gap:18px;font-size:15px;color:#444}
.foot-row .ring{width:56px;height:56px;border:1.5px solid #bbb;border-radius:50%;position:relative}
.foot-row .ring::after{content:"";position:absolute;left:22px;top:22px;width:10px;height:10px;border-radius:50%;background:var(--green)}
.detail{position:absolute;left:778px;font-size:15px;line-height:24px;color:#444;display:flex;gap:10px}
.detail svg{flex:none;margin-top:5px}
.bottom-bar{position:absolute;left:0;top:4775px;width:1200px;height:75px;background:var(--teal-dark)}
</style>
</head>
<body>

<!-- header -->
<header>
  <div class="brand"><span class="mark"></span>ORVET</div>
  <div class="pill teal" style="left:598px;top:12px;width:140px;height:46px;font-size:15px">Join ORVET</div>
  <div class="pill yellow" style="left:745px;top:12px;width:190px;height:46px;font-size:15px">Donate to ORVET</div>
  <div class="social-top" style="left:946px"><span></span><span></span><span></span></div>
  <nav class="nav"><span>About</span><span>Programs</span><span>Rehabilitation and Sports</span><span>Rights Realization</span><span>News</span><span>Contact Us</span></nav>
</header>

<!-- hero -->
<section>
  <div class="hero-panel"></div>
  <div class="hero-rule"></div>
  <h1 class="hero-title serif">A good life<br>for everyone,<br>like everyone</h1>
  <div class="pill yellow" style="left:110px;top:522px;width:353px;height:70px;font-size:17px">Donate to help us help them</div>
  <div class="photo" role="img" aria-label="Smiling young woman in a wheelchair laughing with a volunteer in a classroom" style="left:482px;top:118px;width:718px;height:602px;background:linear-gradient(120deg,#2f3a36 0%,#6f6a5c 40%,#c9c0b0 70%,#3c4a48 100%)"></div>
</section>

<!-- I want to know -->
<section class="want">
  <h2 class="section-title" style="top:65px">I Want To Know</h2>
  <svg class="abs" style="left:0;top:0" width="1200" height="530" viewBox="0 0 1200 530">
    <g fill="#fff">
      <polygon points="60,370 230,150 350,400"/>
      <polygon points="375,160 625,240 395,420"/>
      <polygon points="630,360 720,150 890,370"/>
      <polygon points="890,400 1020,140 1150,375"/>
    </g>
    <polygon points="178,238 240,152 205,155" fill="#0b6b5f"/>
    <polygon points="262,180 285,195 262,198" fill="#0b6b5f"/>
    <polygon points="372,390 400,470 420,400" fill="#3aaa47"/>
    <polygon points="710,155 780,150 760,225" fill="#1fb6b1"/>
    <polygon points="660,180 690,172 688,188" fill="#1fb6b1"/>
    <polygon points="1105,320 1175,370 1140,380" fill="#e8b20e"/>
    <polygon points="1112,392 1145,390 1115,420" fill="#e8b20e"/>
  </svg>
  <div class="tri-text" style="left:137px;top:256px">what are all the rights available to people with physical disabilities and their families</div>
  <div class="tri-text" style="left:385px;top:256px">where I can join online classes offered by ORVET</div>
  <div class="tri-text" style="left:640px;top:256px">what services there are for children with disabilities</div>
  <div class="tri-text" style="left:943px;top:256px">if there is a rehabilitation center in my area</div>
</section>

<!-- services band (behind about) -->
<section class="services">
  <div class="eyebrow" style="position:absolute;width:100%;text-align:center;top:118px;color:#fff">Services</div>
  <h2 class="section-title" style="top:150px;color:#fff">What We Offer</h2>
</section>

<!-- about -->
<section>
  <div class="photo" role="img" aria-label="Young man on a yellow beach wheelchair with volunteers at the seashore" style="left:110px;top:1250px;width:524px;height:528px;background:linear-gradient(160deg,#b9c7cf 0%,#8fa4ad 40%,#c8b48a 75%,#a68c5e 100%)"></div>
  <div class="about-card">
    <div class="eyebrow" style="position:absolute;left:44px;top:46px">About Us</div>
    <h2 class="h2" style="position:absolute;left:44px;top:76px">Who We Are</h2>
    <p class="body-text" style="position:absolute;left:44px;top:142px;width:385px">The Orvet Association strives to enable people with physical disabilities to live meaningful and high-quality lives.</p>
    <p class="body-text" style="position:absolute;left:44px;top:246px;width:385px">Since 1952, spurred by the polio virus outbreak, ORVET has been providing a wide range of activities for children and adults with disabilities to enable them to live independently and integrate into society.</p>
    <div class="pill yellow" style="left:44px;top:410px;width:154px;height:58px;font-size:16px">Read more</div>
  </div>
  <svg class="abs" style="left:900px;top:1720px" width="190" height="60" viewBox="0 0 190 60">
    <polygon points="5,58 40,4 75,58" fill="#3aaa47"/>
    <polygon points="160,30 190,10 190,45" fill="#fff"/>
  </svg>
</section>

<!-- service cards -->
<article class="card" style="left:15px">
  <div class="img" role="img" aria-label="Smiling student holding a teal folder" style="background:linear-gradient(135deg,#d9a13a,#6b4d2a)"></div>
  <h3>Education</h3>
  <p>ORVET works to impart education and knowledge to people with disabilities and operates the dedicated campus ...</p>
</article>
<article class="card" style="left:312px">
  <div class="img" role="img" aria-label="Adaptive swimming competition at an indoor pool" style="background:linear-gradient(135deg,#2a4fa8,#9bb0d8)"></div>
  <h3>Sports and Rehab</h3>
  <p>ORVET encourages people with disabilities to play sports and find new strengths in themselves...</p>
</article>
<article class="card" style="left:609px">
  <div class="img" role="img" aria-label="Group hiking together along a dirt trail" style="background:linear-gradient(180deg,#cfd9dd,#9aa37a 60%,#b9a27c)"></div>
  <h3>Rights Realization</h3>
  <p>ORVET promotes policies concerning people with physical-motor disabilities, promotes their rights, ...</p>
</article>
<article class="card" style="left:906px">
  <div class="img" role="img" aria-label="Cheerful group in wheelchairs celebrating at a community center" style="background:linear-gradient(135deg,#e8e4de,#8c8c8c 60%,#b3463c)"></div>
  <h3>Community infrastructure</h3>
  <p>ORVET owns the association's houses all over the country, rehabilitation day centers,...</p>
</article>

<!-- banner -->
<section>
  <div class="photo" role="img" aria-label="Two smiling women posing together in an art workshop" style="left:0;top:2452px;width:1200px;height:516px;background:linear-gradient(90deg,#2b2622 0%,#3d332c 45%,#6a5747 70%,#2f6e5c 100%)"></div>
  <h2 class="banner-title">Even people with disabilities<br>can be with everyone,<br>like everyone</h2>
  <div class="pill yellow" style="left:107px;top:2740px;width:209px;height:72px;font-size:18px">Donate now</div>
  <div class="abs" style="left:107px;top:2848px;font-size:18px;font-style:italic;font-weight:500;color:#fff">Don't leave them behind</div>
</section>

<!-- news & locations -->
<section>
  <div class="eyebrow abs" style="left:110px;top:3042px">Post</div>
  <h2 class="h2 abs" style="left:110px;top:3075px">Latest News</h2>
  <div class="news-item" style="top:3155px">
    <div class="thumb" role="img" aria-label="Group walking on a trail" style="background:linear-gradient(135deg,#9fb3c4,#3c5a8a)"></div>
    <h4>Duis aute irure dolor in repre hen</h4>
    <div class="date"><i></i>20/11/2023</div>
  </div>
  <div class="news-item" style="top:3318px">
    <div class="thumb" role="img" aria-label="Friends in wheelchairs at a gathering" style="background:linear-gradient(135deg,#c7d84a,#4b5a3a)"></div>
    <h4>Duis aute irure dolor in repre hen</h4>
    <div class="date"><i></i>20/11/2023</div>
  </div>
  <div class="news-item" style="top:3482px">
    <div class="thumb" role="img" aria-label="Beach wheelchair outing by the sea" style="background:linear-gradient(135deg,#b9c7cf,#d4a52a)"></div>
    <h4>Duis aute irure dolor in repre hen</h4>
    <div class="date"><i></i>20/11/2023</div>
  </div>

  <div class="eyebrow abs" style="left:628px;top:3042px">Map</div>
  <h2 class="h2 abs" style="left:628px;top:3075px">Our Locations</h2>
  <div class="photo" role="img" aria-label="Regional map marking the association's center locations" style="left:628px;top:3155px;width:462px;height:490px;background:linear-gradient(90deg,#d8ecee 0%,#d8ecee 40%,#5fcfdc 55%,#e6ece8 75%)"></div>
</section>

<!-- contact -->
<section class="contact">
  <div class="eyebrow" style="position:absolute;width:100%;text-align:center;top:78px">Get In Touch</div>
  <h2 class="section-title" style="top:110px">Contact Us</h2>
  <div class="field" style="left:173px;top:190px;width:417px;height:50px">Name(*)</div>
  <div class="field" style="left:173px;top:255px;width:417px;height:50px">Email(*)</div>
  <div class="field" style="left:173px;top:320px;width:417px;height:50px">Phone(*)</div>
  <div class="field" style="left:600px;top:190px;width:427px;height:180px">Message</div>
  <div class="abs" style="left:178px;top:402px;width:15px;height:15px;border:1.5px solid #555;background:#fff"></div>
  <p class="abs" style="left:204px;top:398px;width:600px;font-size:14px;line-height:26px;color:#444">I know that the details I provided are stored in Orvet's databases, subject to the rules of privacy protection and information security and in accordance with the privacy policy detailed on the website</p>
  <div class="pill yellow" style="left:530px;top:510px;width:138px;height:60px;font-size:16px">Submit</div>
</section>

<!-- footer -->
<footer>
  <div class="brand" style="top:4440px;font-size:40px"><span class="mark" style="width:28px;height:28px"></span>ORVET</div>
  <p class="abs" style="left:110px;top:4590px;width:380px;font-size:15px;line-height:26px;color:#444">We operate a Center for the Rights Realization of people with physical disabilities and family members!</p>

  <div class="foot-head" style="left:555px;top:4440px">Social Media</div>
  <div class="foot-row" style="left:555px;top:4488px"><span class="ring"></span>Circleup</div>
  <div class="foot-row" style="left:555px;top:4552px"><span class="ring"></span>Worknet</div>
  <div class="foot-row" style="left:555px;top:4616px"><span class="ring"></span>Snapgrid</div>

  <div class="foot-head" style="left:778px;top:4440px">Contact Details</div>
  <div class="detail" style="top:4488px"><svg width="16" height="12" viewBox="0 0 16 12"><rect x="0.5" y="0.5" width="15" height="11" fill="#3aaa47"/><path d="M1 1l7 6 7-6" stroke="#fff" fill="none"/></svg>hello@orvet-care.org</div>
  <div class="detail" style="top:4536px"><svg width="14" height="14" viewBox="0 0 14 14"><path d="M3 1l3 3-2 2a8 8 0 0 0 4 4l2-2 3 3-2 2C6 13 1 8 1 3z" fill="#3aaa47"/></svg>03-5550147</div>
  <div class="detail" style="top:4584px"><svg width="14" height="14" viewBox="0 0 14 14"><rect x="1" y="4" width="12" height="9" fill="#3aaa47"/><rect x="3" y="1" width="8" height="4" fill="#3aaa47"/></svg>03-5550148</div>
  <div class="detail" style="top:4636px"><svg width="12" height="16" viewBox="0 0 12 16"><path d="M6 0a6 6 0 0 1 6 6c0 4-6 10-6 10S0 10 0 6a6 6 0 0 1 6-6z" fill="#3aaa47"/><circle cx="6" cy="6" r="2" fill="#fff"/></svg><span>5 Cedar Lane<br>&nbsp;&nbsp;&nbsp;PO Box 4410<br>&nbsp;&nbsp;&nbsp;Harbor Town&nbsp; 4800217</span></div>

  <div class="bottom-bar">
    <div class="abs" style="left:0;width:100%;top:26px;text-align:center;font-size:15px;color:#fff">© 2023, ORVET Association. All rights reserved.</div>
    <svg class="abs" style="left:1052px;top:20px" width="36" height="36" viewBox="0 0 36 36"><circle cx="18" cy="18" r="16" fill="none" stroke="#fff" stroke-width="2.5"/><path d="M18 26V11M12 17l6-6 6 6" stroke="#fff" stroke-width="2.5" fill="none"/></svg>
  </div>
</footer>

</body>
</html>
```